Design luxury business card layout
simple but slick business card layout
Professional
Rupert Calloway or Dorsan Mbeki
creative director
Whitcombe Court House
Whitcombe Court
Mayfair
London
W1K 4RT
Info@velmorabyte.com
www.velmorabyte.com
Please can all appplicants take notice of the images provided as a guide.
We will be giving feed back on a daily basis
so please check up on any updates
The reverse side of the business card will only have our logo and monogram which is one of our most important concerns . We will provide pictures as a guide which will include colour schemes etc
our Material will be similar to this

```html
<!DOCTYPE html>
<html lang="en">
<head>
<meta charset="utf-8">
<title>Velmora Byte — Business Card</title>
<link href="https://fonts.googleapis.com/css2?family=Montserrat:wght@300;400&family=Open+Sans:wght@400;600;700&display=swap" rel="stylesheet">
<style>
  :root {
    --stage: #2b2b2b;
    --card: #0b0b0b;
    --card-edge: #1c1c1c;
    --gold: #e0b12e;
    --text-light: #d6d6d6;
    --text-muted: #8a8a8a;
    --pattern: #161616;
    --pattern-hi: #222222;
  }
  * { margin: 0; padding: 0; box-sizing: border-box; }
  html, body { width: 1200px; height: 901px; overflow: hidden; }
  body {
    background: var(--stage);
    font-family: "Open Sans", Arial, sans-serif;
    display: flex;
    flex-direction: column;
    align-items: center;
    justify-content: center;
    gap: 56px;
  }
  .card {
    position: relative;
    width: 620px;
    height: 354px;
    border-radius: 22px;
    background: linear-gradient(150deg, #161616 0%, var(--card) 45%, #050505 100%);
    border: 1px solid var(--card-edge);
    box-shadow: 0 14px 30px rgba(0,0,0,.55);
    overflow: hidden;
  }

  /* reverse side */
  .card-back .pattern-band {
    position: absolute;
    left: 0; right: 0;
    height: 112px;
    background: linear-gradient(160deg, var(--pattern-hi) 0%, var(--pattern) 100%);
  }
  .card-back .pattern-top { top: 0; }
  .card-back .pattern-bottom { bottom: 0; }
  .card-back .logo-band {
    position: absolute;
    top: 112px; left: 0; right: 0;
    height: 130px;
    background: var(--card);
    display: flex;
    flex-direction: column;
    align-items: center;
    justify-content: center;
    gap: 14px;
  }
  .brand-dot {
    width: 44px; height: 44px;
    border-radius: 50%;
    background: var(--text-light);
  }
  .brand-name {
    font-family: "Montserrat", Arial, sans-serif;
    font-weight: 300;
    color: var(--text-light);
    letter-spacing: .42em;
    font-size: 15px;
  }

  /* front side */
  .card-front .front-logo {
    position: absolute;
    top: 34px; left: 44px;
    display: flex;
    flex-direction: column;
    align-items: center;
    gap: 12px;
  }
  .card-front .front-logo .brand-dot { width: 36px; height: 36px; }
  .card-front .front-logo .brand-name { font-size: 13px; }
  .gold-tab {
    position: absolute;
    left: 0; top: 150px;
    width: 8px; height: 30px;
    background: var(--gold);
  }
  .holder {
    position: absolute;
    top: 118px; right: 42px;
    text-align: right;
  }
  .holder-name {
    color: var(--gold);
    font-weight: 700;
    font-size: 21px;
  }
  .holder-role {
    color: var(--text-muted);
    font-size: 12px;
    margin-top: 2px;
  }
  .address {
    position: absolute;
    top: 158px; left: 44px;
    color: var(--text-muted);
    font-size: 12px;
    font-style: normal;
    line-height: 1.45;
  }
  .contacts {
    position: absolute;
    top: 226px; left: 44px;
    list-style: none;
    color: var(--text-muted);
    font-size: 12px;
    line-height: 1.5;
  }
  .contacts li { display: flex; align-items: center; gap: 8px; }
  .contacts svg { width: 12px; height: 12px; fill: var(--gold); flex: none; }
  .website {
    position: absolute;
    bottom: 30px; left: 44px;
    color: var(--text-muted);
    font-size: 13px;
    letter-spacing: .12em;
  }
  .website strong { color: var(--gold); font-weight: 700; }
</style>
</head>
<body>

  <section class="card card-back" aria-label="Card reverse">
    <div class="pattern-band pattern-top" role="img" aria-label="Glossy black geometric pattern band"></div>
    <div class="logo-band">
      <span class="brand-dot"></span>
      <span class="brand-name">VELMORA BYTE</span>
    </div>
    <div class="pattern-band pattern-bottom" role="img" aria-label="Glossy black geometric pattern band"></div>
  </section>

  <section class="card card-front" aria-label="Card front">
    <div class="front-logo">
      <span class="brand-dot"></span>
      <span class="brand-name">VELMORA BYTE</span>
    </div>
    <span class="gold-tab"></span>

    <div class="holder">
      <p class="holder-name">Rupert Calloway</p>
      <p class="holder-role">Creative Director</p>
    </div>

    <address class="address">
      Whitcombe Court House<br>
      Whitcombe Court, Mayfair,<br>
      London, W1K 4RT
    </address>

    <ul class="contacts">
      <li><svg viewBox="0 0 12 12"><path d="M2 1h3l1 3-1.5 1a7 7 0 0 0 2.5 2.5L8 6l3 1v3a1 1 0 0 1-1 1A9 9 0 0 1 1 2a1 1 0 0 1 1-1z"/></svg>+44 (0) 207 946 0381</li>
      <li><svg viewBox="0 0 12 12"><path d="M3 0h6a1 1 0 0 1 1 1v10a1 1 0 0 1-1 1H3a1 1 0 0 1-1-1V1a1 1 0 0 1 1-1zm0 2v7h6V2z"/></svg>+44 (0) 7700 900 412</li>
      <li><svg viewBox="0 0 12 12"><path d="M0 2h12v8H0zm1 1v.5l5 3 5-3V3z"/></svg>Info@velmorabyte.com</li>
    </ul>

    <p class="website">www.<strong>velmorabyte</strong>.com</p>
  </section>

</body>
</html>
```